Tech Company Office Internal Feature Wall Ultra HighRes - Wall Paper Design

We need a graphic designer to come up with a cool design for an internal feature wall in our new office. Dimensions of the wall can be found in the PDF file “Interior Wall Dimensions.pdf”. We are a technology consultancy firm based in Perth, Western Australia that provides a number of IT services including datacentre/cloud services, software development, cyber security, managed services and more.

The vibe we are looking to go with is innovation, cutting edge, technology, cyber, revolutionary. When people see the feature wall it should scream “cutting edge” tech company.

With regards to the contents of the image, this is up to the designer however we would like to ask our logo to be featured on the wall somewhere (we uploaded two different logo samples of different layout in vector format).

As this will be printed large scale into wallpaper, the finished design must be extremely high resolution to ensure zero distorted pixilation during printing. We provided the dimensions of the wall under the PDF file “Interior Wall Dimensions.pdf”.

I have uploaded some photos of the wall (the desks/shelves in front of the wall will be moved).

I would love to see the designs that are uploaded.

```html
<!DOCTYPE html>
<html lang="en">
<head>
<meta charset="utf-8">
<title>Novaridge Technologies – Feature Wall</title>
<link rel="stylesheet" href="https://fonts.googleapis.com/css2?family=Roboto+Condensed:wght@400&family=Montserrat:wght@600&display=swap">
<style>
  :root {
    --wall-grey: #f1f2f2;
    --navy: #1b2a6e;
    --steel: #8d9093;
    --collage-deep: #1f5d97;
    --collage-blue: #2f7fb8;
    --collage-teal: #2aa39a;
    --collage-green: #3bb58a;
    --wave-cyan: #5cc6dc;
    --globe-blue: #3b8fc9;
    --globe-teal: #33b3a6;
    --white: #ffffff;
  }
  * { margin: 0; padding: 0; box-sizing: border-box; }
  html, body {
    width: 1200px;
    height: 404px;
    overflow: hidden;
    background: var(--white);
  }
  .feature-wall {
    position: relative;
    width: 1200px;
    height: 404px;
    overflow: hidden;
    background: linear-gradient(90deg, var(--wall-grey) 0%, #eeeff0 60%, #f6f7f7 80%, #e9eef0 100%);
  }

  /* Left photo collage */
  .photo-collage {
    position: absolute;
    left: 0; top: 0;
    width: 374px; height: 404px;
    background: linear-gradient(180deg, var(--collage-deep) 0%, var(--collage-blue) 32%, var(--collage-teal) 68%, var(--collage-green) 100%);
  }
  .collage-tiles,
  .collage-rings,
  .wave-field {
    position: absolute;
    left: 0; top: 0;
  }
  .collage-divider {
    position: absolute;
    left: 374px; top: 0;
    width: 3px; height: 404px;
    background: var(--white);
  }
  .tagline {
    position: absolute;
    left: 0; top: 148px;
    width: 366px;
    text-align: center;
    font-family: "Roboto Condensed", sans-serif;
    font-weight: 400;
    font-size: 23.5px;
    line-height: 38px;
    color: var(--white);
    text-transform: uppercase;
  }

  /* Right globe graphic */
  .globe-glow {
    position: absolute;
    left: 880px; top: 60px;
    width: 200px; height: 300px;
    background: radial-gradient(ellipse at 70% 50%, rgba(255,255,255,0.95) 0%, rgba(255,255,255,0) 70%);
  }
  .globe {
    position: absolute;
    left: 962px; top: -70px;
    width: 360px; height: 450px;
    border-radius: 50%;
    background:
      radial-gradient(ellipse at 70% 15%, #e8f4f8 0%, rgba(232,244,248,0) 40%),
      linear-gradient(160deg, #9fd0e6 0%, var(--globe-blue) 40%, #2f72b3 60%, var(--globe-teal) 85%, #2a8f8a 100%);
  }

  /* Brand name */
  .brand-mark {
    position: absolute;
    left: 647px; top: 118px;
    width: 70px; height: 70px;
    border-radius: 50%;
    background: var(--navy);
  }
  .brand {
    position: absolute;
    left: 540px; top: 238px;
    width: 284px;
    text-align: center;
    font-family: "Montserrat", sans-serif;
    font-weight: 600;
    color: var(--navy);
  }
  .brand-name {
    display: block;
    font-size: 33px;
    line-height: 34px;
    letter-spacing: 0.5px;
  }
  .brand-sub {
    display: block;
    margin-top: 1px;
    font-size: 13.5px;
    line-height: 18px;
    letter-spacing: 8px;
    padding-left: 8px;
  }
</style>
</head>
<body>
  <main class="feature-wall">
    <div class="photo-collage" role="img" aria-label="Collage of technology photos: eye scan with a lock icon, data centre server aisle, team working at computers, server hardware and a scientist with a sample, tinted blue to green"></div>

    <svg class="collage-tiles" width="374" height="404" viewBox="0 0 374 404" aria-hidden="true">
      <rect x="0" y="0" width="125" height="133" fill="#ffffff" fill-opacity="0.06"/>
      <rect x="126" y="0" width="248" height="133" fill="#0e3f7a" fill-opacity="0.18"/>
      <rect x="0" y="134" width="160" height="136" fill="#ffffff" fill-opacity="0.08"/>
      <rect x="161" y="134" width="213" height="136" fill="#0e4f6e" fill-opacity="0.12"/>
      <rect x="0" y="271" width="205" height="133" fill="#0e4f6e" fill-opacity="0.12"/>
      <rect x="206" y="271" width="168" height="133" fill="#ffffff" fill-opacity="0.07"/>
    </svg>

    <svg class="collage-rings" width="374" height="404" viewBox="0 0 374 404" aria-hidden="true">
      <circle cx="182" cy="200" r="121" fill="none" stroke="#ffffff" stroke-opacity="0.8" stroke-width="1.4"/>
      <circle cx="186" cy="197" r="118" fill="none" stroke="#ffffff" stroke-opacity="0.55" stroke-width="1.1"/>
    </svg>

    <p class="tagline">Pushing the boundaries<br>of technology</p>

    <div class="collage-divider"></div>

    <svg class="wave-field" width="1200" height="404" viewBox="0 0 1200 404" role="img" aria-label="Flowing waves of cyan dots sweeping across the wall">
      <defs>
        <linearGradient id="wave-upper-fill" x1="0" y1="0" x2="1" y2="0.4">
          <stop offset="0" stop-color="#5cc6dc" stop-opacity="0.55"/>
          <stop offset="0.5" stop-color="#5cc6dc" stop-opacity="0.35"/>
          <stop offset="1" stop-color="#5cc6dc" stop-opacity="0"/>
        </linearGradient>
        <linearGradient id="wave-fan-fill" x1="0" y1="0" x2="0" y2="1">
          <stop offset="0" stop-color="#5cc6dc" stop-opacity="0.35"/>
          <stop offset="1" stop-color="#5cc6dc" stop-opacity="0"/>
        </linearGradient>
        <linearGradient id="wave-lower-fill" x1="0" y1="1" x2="1" y2="0">
          <stop offset="0" stop-color="#5cc6dc" stop-opacity="0.1"/>
          <stop offset="0.45" stop-color="#5cc6dc" stop-opacity="0.5"/>
          <stop offset="1" stop-color="#5cc6dc" stop-opacity="0.15"/>
        </linearGradient>
      </defs>
      <path d="M378 60 C450 40 520 20 560 0 L820 0 C740 40 640 50 560 70 C500 80 440 80 378 78 Z" fill="url(#wave-upper-fill)"/>
      <path d="M378 90 C470 90 560 80 650 40 C700 20 740 5 760 0 L800 0 C720 60 620 120 540 170 C480 210 430 250 380 280 Z" fill="url(#wave-fan-fill)"/>
      <path d="M610 404 C700 370 760 320 820 280 C880 240 940 200 1000 180 L1010 200 C950 230 900 290 850 330 C800 370 760 395 720 404 Z" fill="url(#wave-lower-fill)"/>
      <path d="M780 404 C850 380 900 350 950 320 C990 300 1030 290 1060 285 L1060 310 C1010 320 960 350 920 380 C900 392 880 400 860 404 Z" fill="url(#wave-lower-fill)" opacity="0.7"/>
    </svg>

    <div class="globe-glow" aria-hidden="true"></div>
    <div class="globe" role="img" aria-label="Glossy blue and teal digital globe wrapped in circuit-like bands"></div>

    <div class="brand-mark" aria-hidden="true"></div>
    <div class="brand">
      <span class="brand-name">NOVARIDGE</span>
      <span class="brand-sub">TECHNOLOGIES</span>
    </div>
  </main>
</body>
</html>
```